Brenton Wealth Management Flow Charts

I need help creating three flow charts for my businesses website. We want them to be simple but look professional. This is for a Wealth Management firm. I will attach a word document that has all of the descriptions for everything so you know what icons to use. We just want the chart to have an icon, the names of each step and the corresponding numbers. I will also include some examples of charts we liked as well. Once the winner is selected, we will need help with additional graphic design elements for our website ASAP.
- Goudy Roman

```html
<!DOCTYPE html>
<html lang="en">
<head>
<meta charset="utf-8">
<title>Process Flow Charts</title>
<link href="https://fonts.googleapis.com/css2?family=Bebas+Neue&family=Montserrat:wght@500;700&family=Source+Sans+3:wght@300;400&display=swap" rel="stylesheet">
<style>
  :root{
    --c-start:#1aaeb5; --c-discover:#1787a5; --c-plan:#2a5068;
    --c-solution:#6a86b5; --c-impl:#4d5a78; --c-monitor:#333a45;
    --c-idea:#6a91be; --c-promo:#fcb44f; --c-growth:#0cb89a;
    --c-orange:#f6951f; --c-pink:#ec068d; --c-sky:#00aeef; --c-navy:#2b3990;
    --ink:#111; --paper:#fff;
  }
  html,body{margin:0;padding:0;overflow:hidden;background:var(--paper);}
  .canvas{position:relative;width:1200px;height:1031px;overflow:hidden;background:var(--paper);}
  .canvas svg{position:absolute;left:0;top:0;}
  .stage-label{font-family:'Montserrat',sans-serif;font-weight:500;font-size:5px;fill:#fff;text-anchor:middle;}
  .stage-copy{font-family:'Montserrat',sans-serif;font-size:3.4px;fill:#fff;opacity:.85;text-anchor:middle;}
  .flow-title{font-family:'Bebas Neue',sans-serif;font-size:23px;fill:#fff;text-anchor:middle;letter-spacing:.5px;}
  .flow-copy{font-family:'Montserrat',sans-serif;font-weight:700;font-size:7.4px;fill:#fff;text-anchor:middle;letter-spacing:.9px;}
  .card-step{font-family:'Source Sans 3',sans-serif;font-weight:400;font-size:18px;fill:var(--ink);text-anchor:middle;}
  .card-num{font-family:'Source Sans 3',sans-serif;font-weight:400;font-size:42px;fill:var(--ink);text-anchor:middle;}
  .card-head{font-family:'Source Sans 3',sans-serif;font-weight:400;font-size:14px;fill:var(--ink);text-anchor:middle;}
  .card-sub{font-family:'Source Sans 3',sans-serif;font-weight:400;font-size:10px;fill:var(--ink);text-anchor:middle;letter-spacing:2.6px;}
  .card-copy{font-family:'Source Sans 3',sans-serif;font-weight:400;font-size:7.4px;fill:var(--ink);text-anchor:middle;}
</style>
</head>
<body>
<div class="canvas">
<svg width="1200" height="1031" viewBox="0 0 1200 1031" xmlns="http://www.w3.org/2000/svg">
  <defs>
    <filter id="soft-shadow" x="-20%" y="-20%" width="150%" height="150%">
      <feDropShadow dx="5" dy="6" stdDeviation="4" flood-color="#000" flood-opacity=".18"/>
    </filter>
    <g id="stage-copy">
      <text class="stage-copy" x="53" y="57">Lorem ipsum dolor sit amet, consectetuer</text>
      <text class="stage-copy" x="53" y="61">adipiscing elit, sed diam nonummy nibh</text>
      <text class="stage-copy" x="53" y="65">euismod tincidunt laoreet dolore</text>
      <text class="stage-copy" x="53" y="69">magna aliquam erat</text>
      <text class="stage-copy" x="53" y="73">volutpat.</text>
    </g>
  </defs>

  <!-- Process stages row -->
  <g class="stages">
    <g transform="translate(56,138)" filter="url(#soft-shadow)">
      <rect width="106" height="87" rx="14" fill="var(--c-start)"/>
      <circle cx="53" cy="21" r="10" fill="none" stroke="#fff" stroke-width="3.5"/>
      <rect x="51" y="21" width="4" height="13" rx="1.5" fill="#fff"/>
      <line x1="19" y1="43" x2="87" y2="43" stroke="#fff" stroke-width=".6"/>
      <text class="stage-label" x="53" y="51">START</text>
      <use href="#stage-copy"/>
    </g>
    <g transform="translate(248,138)" filter="url(#soft-shadow)">
      <rect width="106" height="87" rx="14" fill="var(--c-discover)"/>
      <circle cx="56" cy="22" r="8" fill="none" stroke="#fff" stroke-width="2.5"/>
      <line x1="50" y1="28" x2="43" y2="35" stroke="#fff" stroke-width="3.5" stroke-linecap="round"/>
      <line x1="19" y1="43" x2="87" y2="43" stroke="#fff" stroke-width=".6"/>
      <text class="stage-label" x="53" y="51">DISCOVER</text>
      <use href="#stage-copy"/>
    </g>
    <g transform="translate(443,138)" filter="url(#soft-shadow)">
      <rect width="106" height="87" rx="14" fill="var(--c-plan)"/>
      <circle cx="53" cy="22" r="7" fill="none" stroke="#fff" stroke-width="2"/>
      <rect x="50" y="29" width="6" height="5" rx="1" fill="#fff"/>
      <g stroke="#fff" stroke-width="1.3" stroke-linecap="round">
        <line x1="53" y1="7" x2="53" y2="10"/><line x1="41" y1="22" x2="38" y2="22"/><line x1="65" y1="22" x2="68" y2="22"/>
        <line x1="44" y1="13" x2="42" y2="11"/><line x1="62" y1="13" x2="64" y2="11"/>
      </g>
      <line x1="19" y1="43" x2="87" y2="43" stroke="#fff" stroke-width=".6"/>
      <text class="stage-label" x="53" y="51">PLAN</text>
      <use href="#stage-copy"/>
    </g>
    <g transform="translate(643,138)" filter="url(#soft-shadow)">
      <rect width="106" height="87" rx="14" fill="var(--c-solution)"/>
      <path d="M45 20 A9 9 0 0 1 60 15" fill="none" stroke="#fff" stroke-width="2.5"/>
      <path d="M61 25 A9 9 0 0 1 46 30" fill="none" stroke="#fff" stroke-width="2.5"/>
      <path d="M57 11 L63 14 L58 19 Z M49 34 L43 31 L48 26 Z" fill="#fff"/>
      <line x1="19" y1="43" x2="87" y2="43" stroke="#fff" stroke-width=".6"/>
      <text class="stage-label" x="53" y="51">SOLUTION</text>
      <use href="#stage-copy"/>
    </g>
    <g transform="translate(836,138)" filter="url(#soft-shadow)">
      <rect width="106" height="87" rx="14" fill="var(--c-impl)"/>
      <circle cx="47" cy="25" r="8" fill="none" stroke="#fff" stroke-width="4" stroke-dasharray="3 2"/>
      <circle cx="47" cy="25" r="4.5" fill="none" stroke="#fff" stroke-width="2.5"/>
      <circle cx="62" cy="16" r="5" fill="none" stroke="#fff" stroke-width="2.5" stroke-dasharray="2 1.5"/>
      <circle cx="62" cy="16" r="2" fill="#fff"/>
      <line x1="19" y1="43" x2="87" y2="43" stroke="#fff" stroke-width=".6"/>
      <text class="stage-label" x="53" y="51">IMPLEMENTATION</text>
      <use href="#stage-copy"/>
    </g>
    <g transform="translate(1036,138)" filter="url(#soft-shadow)">
      <rect width="106" height="87" rx="14" fill="var(--c-monitor)"/>
      <g fill="#fff">
        <rect x="41" y="28" width="4" height="6"/><rect x="47" y="24" width="4" height="10"/>
        <rect x="53" y="20" width="4" height="14"/><rect x="59" y="16" width="4" height="18"/>
      </g>
      <path d="M40 22 L48 16 L53 18 L62 10" fill="none" stroke="#fff" stroke-width="1.6"/>
      <path d="M59 9 L64 8 L63 13 Z" fill="#fff"/>
      <line x1="19" y1="43" x2="87" y2="43" stroke="#fff" stroke-width=".6"/>
      <text class="stage-label" x="53" y="51">MONITOR &amp; ADAPT</text>
      <use href="#stage-copy"/>
    </g>
    <g class="stage-links" stroke="#8a96a8" stroke-width="1.5">
      <line x1="187" y1="189" x2="220" y2="189"/><circle cx="187" cy="189" r="6" fill="var(--c-start)" stroke="none"/><circle cx="220" cy="189" r="6" fill="var(--c-discover)" stroke="none"/>
      <line x1="382" y1="189" x2="416" y2="189"/><circle cx="382" cy="189" r="6" fill="var(--c-discover)" stroke="none"/><circle cx="416" cy="189" r="6" fill="var(--c-plan)" stroke="none"/>
      <line x1="579" y1="189" x2="613" y2="189"/><circle cx="579" cy="189" r="6" fill="var(--c-plan)" stroke="none"/><circle cx="613" cy="189" r="6" fill="var(--c-solution)" stroke="none"/>
      <line x1="775" y1="189" x2="809" y2="189"/><circle cx="775" cy="189" r="6" fill="var(--c-solution)" stroke="none"/><circle cx="809" cy="189" r="6" fill="var(--c-impl)" stroke="none"/>
      <line x1="971" y1="189" x2="1006" y2="189"/><circle cx="971" cy="189" r="6" fill="var(--c-impl)" stroke="none"/><circle cx="1006" cy="189" r="6" fill="var(--c-monitor)" stroke="none"/>
    </g>
  </g>

  <!-- Idea / Promotion / Growth flow -->
  <g class="flow" fill="none" stroke-width="3">
    <g stroke="var(--c-idea)">
      <path d="M245 413 V316 Q245 307 254 307 H449 Q458 307 458 316 V413 H483"/>
      <path d="M245 425 V511 Q245 520 254 520 H449 Q458 520 458 511 V425" stroke-dasharray="7 8"/>
      <path d="M482 406 L495 413 L482 420 Z" fill="var(--c-idea)" stroke="none"/>
    </g>
    <g stroke="var(--c-promo)">
      <path d="M494 413 V511 Q494 520 503 520 H698 Q707 520 707 511 V413 H733"/>
      <path d="M494 403 V316 Q494 307 503 307 H698 Q707 307 707 316 V403" stroke-dasharray="7 8"/>
      <path d="M731 406 L744 413 L731 420 Z" fill="var(--c-promo)" stroke="none"/>
    </g>
    <g stroke="var(--c-growth)">
      <path d="M744 413 V316 Q744 307 753 307 H948 Q957 307 957 316 V413"/>
      <path d="M744 425 V511 Q744 520 753 520 H948 Q957 520 957 511 V425" stroke-dasharray="7 8"/>
    </g>
    <rect x="260" y="322" width="183" height="183" rx="6" fill="#fff" stroke="none" filter="url(#soft-shadow)"/>
    <rect x="509" y="322" width="183" height="183" rx="6" fill="#fff" stroke="none" filter="url(#soft-shadow)"/>
    <rect x="758" y="322" width="183" height="183" rx="6" fill="#fff" stroke="none" filter="url(#soft-shadow)"/>
    <rect x="263" y="325" width="177" height="177" rx="4" fill="var(--c-idea)" stroke="none"/>
    <rect x="512" y="325" width="177" height="177" rx="4" fill="var(--c-promo)" stroke="none"/>
    <rect x="761" y="325" width="177" height="177" rx="4" fill="var(--c-growth)" stroke="none"/>

    <g stroke="#fff" stroke-width="1.4">
      <path d="M343 379 Q336 370 337 366 A11 11 0 1 1 359 366 Q360 370 353 379 Z"/>
      <line x1="344" y1="382" x2="352" y2="382"/><line x1="345" y1="385" x2="351" y2="385"/>
      <rect x="590" y="363" width="24" height="16"/>
      <path d="M590 363 L602 373 L614 363 M590 379 L599 371 M614 379 L605 371"/>
      <path d="M841 364 V384 H862" stroke-width="2.2"/>
      <path d="M844 381 L850 373 L854 377 L861 368" stroke-width="2.2"/>
      <path d="M857 366 L863 366 L863 372" stroke-width="2"/>
    </g>
    <g stroke="none">
      <text class="flow-title" x="348" y="412">IDEA</text>
      <text class="flow-copy" x="351" y="427">Lorem ipsum dolor sit</text>
      <text class="flow-copy" x="351" y="439">amet, consectetur</text>
      <text class="flow-copy" x="351" y="451">adipiscing elit. Fusce</text>
      <text class="flow-copy" x="351" y="464">dignissim pretium</text>
      <text class="flow-title" x="602" y="412">PROMOTION</text>
      <text class="flow-copy" x="602" y="427">Lorem ipsum dolor sit</text>
      <text class="flow-copy" x="602" y="439">amet, consectetur</text>
      <text class="flow-copy" x="602" y="451">adipiscing elit. Fusce</text>
      <text class="flow-copy" x="602" y="464">dignissim pretium</text>
      <text class="flow-title" x="851" y="412">GROWTH</text>
      <text class="flow-copy" x="850" y="427">Lorem ipsum dolor sit</text>
      <text class="flow-copy" x="850" y="439">amet, consectetur</text>
      <text class="flow-copy" x="850" y="451">adipiscing elit. Fusce</text>
      <text class="flow-copy" x="850" y="464">dignissim pretium</text>
    </g>
  </g>

  <!-- Step cards -->
  <defs>
    <g id="card-face">
      <polygon points="153,654 281,645 284,881 153,895" fill="#9a9a9a" stroke="#9a9a9a" stroke-width="60" stroke-linejoin="round"/>
      <polygon points="156,652 281,643 283,876 155,892" fill="#fff" stroke="#fff" stroke-width="60" stroke-linejoin="round"/>
      <line x1="208" y1="810" x2="232" y2="810" stroke="#555" stroke-width=".7"/>
      <text class="card-copy" x="220" y="828">Lorem ipsum dolor sit</text>
      <text class="card-copy" x="220" y="837">amet, consectetuer</text>
      <text class="card-copy" x="220" y="846">adipiscing elit, sed diam</text>
      <text class="card-copy" x="220" y="855">nonummy nibh euismod</text>
      <text class="card-copy" x="220" y="864">tincidunt ut laoreet</text>
      <text class="card-copy" x="220" y="873">dolore magna aliquam</text>
      <text class="card-step" x="220" y="680">STEP</text>
      <text class="card-head" x="220" y="748">YOUR TEXT HERE</text>
      <text class="card-sub" x="220" y="797">YOUR TEXT HERE</text>
    </g>
    <polygon id="card-back" points="120,650 272,616 322,856 150,926" stroke-width="40" stroke-linejoin="round"/>
  </defs>
  <g class="cards">
    <g><use href="#card-back" fill="var(--c-orange)" stroke="var(--c-orange)"/><use href="#card-face"/>
      <text class="card-num" x="218" y="727">01</text><text class="card-head" x="220" y="783">OPTION A</text></g>
    <g transform="translate(240,0)"><use href="#card-back" fill="var(--c-pink)" stroke="var(--c-pink)"/><use href="#card-face"/>
      <text class="card-num" x="220" y="727">02</text><text class="card-head" x="220" y="783">OPTION B</text></g>
    <g transform="translate(488,0)"><use href="#card-back" fill="var(--c-sky)" stroke="var(--c-sky)"/><use href="#card-face"/>
      <text class="card-num" x="220" y="727">03</text><text class="card-head" x="220" y="783">OPTION C</text></g>
    <g transform="translate(754,0)"><use href="#card-back" fill="var(--c-navy)" stroke="var(--c-navy)"/><use href="#card-face"/>
      <text class="card-num" x="220" y="727">04</text><text class="card-head" x="220" y="783">OPTION C</text></g>
  </g>
</svg>
</div>
</body>
</html>
```